Letterhead design for business

Looking for an attractive and professional letterhead that uses the logo that is attached below.

Target Market(s)

Potential bankruptcy clients.

Industry/Entity Type

Legal

Colors

Designer to choose colors to be used in the design.

Requirements
Must have
• Address for locations, phone number, and website address.
• Addresses are on website ferncoveadvice.example. Use following phone number (for tracking purposes): 555-013-8274

```html
<!DOCTYPE html>
<html lang="en">
<head>
<meta charset="utf-8">
<title>Ferncove Advice Law Group – Letterhead</title>
<link rel="stylesheet" href="https://fonts.googleapis.com/css2?family=Exo+2:wght@400&family=Arimo:wght@400&display=swap">
<style>
  :root {
    --backdrop: #dcdcdc;
    --paper: #ffffff;
    --brand-green: #7fc08a;
    --charcoal: #4f4f4f;
    --ink: #3a3a3a;
    --footer-dark: #363636;
    --footer-mid: #4a4a4a;
    --footer-text: #ffffff;
  }
  html, body {
    margin: 0;
    padding: 0;
    width: 1200px;
    height: 1200px;
    overflow: hidden;
    background: var(--backdrop);
  }
  .letterhead {
    position: absolute;
    left: 254px;
    top: 30px;
    width: 693px;
    height: 1140px;
    box-shadow: 0 2px 10px rgba(0,0,0,0.18);
  }
  .letterhead svg { display: block; width: 100%; height: 100%; }
  .brand-name { font-family: "Exo 2", sans-serif; font-size: 40px; fill: var(--ink); }
  .brand-sub { font-family: "Exo 2", sans-serif; font-size: 16px; letter-spacing: 4px; fill: var(--ink); }
  .brand-tagline { font-family: "Exo 2", sans-serif; font-size: 14px; fill: var(--brand-green); }
  .contact-text { font-family: "Arimo", sans-serif; font-size: 15px; fill: var(--footer-text); }
  .contact-icon { fill: none; stroke: var(--footer-text); stroke-width: 1.4; }
</style>
</head>
<body>
  <main class="letterhead">
    <svg viewBox="0 0 796 1310" xmlns="http://www.w3.org/2000/svg">
      <rect class="paper" width="796" height="1310" fill="var(--paper)"/>

      <g class="header-swoosh">
        <path d="M0,0 H620 V110 C440,30 230,20 0,42 Z" fill="var(--brand-green)"/>
        <path d="M150,0 H796 V216 C700,130 520,45 150,0 Z" fill="#3c3c3c" opacity="0.5"/>
        <path d="M160,0 H796 V208 C700,125 520,40 160,0 Z" fill="var(--charcoal)"/>
      </g>

      <g class="brand">
        <circle cx="96" cy="104" r="44" fill="var(--brand-green)"/>
        <line x1="167" y1="50" x2="167" y2="162" stroke="var(--brand-green)" stroke-width="2"/>
        <text class="brand-name" x="184" y="108">Ferncove Advice</text>
        <text class="brand-sub" x="186" y="137">LAW GROUP</text>
        <text class="brand-tagline" x="186" y="160">by Attorney R. Calloway</text>
      </g>

      <g class="contact-bar">
        <rect x="0" y="1247" width="180" height="44" fill="var(--footer-dark)"/>
        <rect x="180" y="1247" width="356" height="44" fill="var(--footer-mid)"/>
        <rect x="536" y="1247" width="260" height="44" fill="var(--footer-dark)"/>
        <rect x="0" y="1294" width="796" height="3" fill="var(--footer-mid)"/>

        <g class="contact-phone">
          <circle class="contact-icon" cx="38" cy="1269" r="9"/>
          <path class="contact-icon" d="M35,1264 q-2,5 3,10 l2,-2"/>
          <text class="contact-text" x="63" y="1274">555-013-8274</text>
        </g>
        <g class="contact-address">
          <circle class="contact-icon" cx="246" cy="1269" r="9"/>
          <path class="contact-icon" d="M246,1274 l-3.5,-5 a3.8,3.8 0 1 1 7,0 z"/>
          <text class="contact-text" x="270" y="1274">Your Address Goes Here</text>
        </g>
        <g class="contact-web">
          <circle class="contact-icon" cx="578" cy="1269" r="9"/>
          <ellipse class="contact-icon" cx="578" cy="1269" rx="4" ry="9"/>
          <line class="contact-icon" x1="569" y1="1269" x2="587" y2="1269"/>
          <text class="contact-text" x="602" y="1274">ferncoveadvice.example</text>
        </g>
      </g>
    </svg>
  </main>
</body>
</html>
```